Bref créative
New Corporate Website - Blue Falcons
Blue Falcons - Marketing & Lead Generation
Marketing
Does not yet exist
Blue Falcons is a new Marketing and Sales Lead generation agency specializing in helping companies analyze, pursue and close sales opportunities generated via the Internet. We provide access to our exclusive Blue Falcon Striker platform for capturing and pursing sales opportunities generated via the online platform.
I'd like to showcase a lot of red on this website. This is a new website for a new company we are starting.
The website is to feature both our online web software as well as our consulting services.
High Tech
Red (#aa0000)
Grey (#cccccc)
Verdana
Century Gothic
top
http://www.vortelix.com
http://www.brinaxo.com/en
http://www.quombrel.com
The page should include links for
Navigation
- About Blue Falcons
- Services & Solutions
- Results
- News & Announcements
- Contact Us
Also, an area for current customer's to login
please incorporate the logo of the man riding the horse backwards.

```html
<!DOCTYPE html>
<html lang="en">
<head>
<meta charset="utf-8">
<title>Blue Falcons – Marketing &amp; Lead Generation</title>
<link href="https://fonts.googleapis.com/css2?family=Didact+Gothic&family=Noto+Sans:ital,wght@0,400;0,700;1,400&display=swap" rel="stylesheet">
<style>
  :root {
    --red: #aa0000;
    --red-deep: #8a0000;
    --red-dark: #6e0000;
    --grey: #cccccc;
    --grey-light: #eeeeee;
    --white: #ffffff;
    --footer-text: #999999;
  }
  * { box-sizing: border-box; margin: 0; padding: 0; }
  html, body { width: 1200px; height: 821px; overflow: hidden; }
  body {
    position: relative;
    background: linear-gradient(to bottom, var(--red) 0, var(--red) 730px, var(--grey-light) 738px, #f7f7f7 821px);
    font-family: "Noto Sans", Verdana, sans-serif;
    color: var(--white);
  }
  .top-nav {
    position: absolute; left: 0; top: 0; width: 1200px; height: 54px;
    background: linear-gradient(to bottom, var(--red-deep), var(--red-dark));
    box-shadow: 0 3px 8px rgba(0,0,0,.35);
  }
  .top-nav ul { list-style: none; }
  .top-nav li { position: absolute; top: 16px; }
  .top-nav a {
    color: var(--white); text-decoration: none; font-size: 18px; white-space: nowrap;
  }
  .nav-about { left: 168px; }
  .nav-services { left: 384px; }
  .nav-results { left: 582px; }
  .nav-news { left: 684px; }
  .nav-contact { left: 943px; }
  .main-panel {
    position: absolute; left: 125px; top: 79px; width: 950px; height: 630px;
    background: linear-gradient(to bottom, #b20000, var(--red) 60%, #a20000);
    border-top: 2px solid rgba(255,255,255,.45);
    box-shadow: 0 6px 22px rgba(0,0,0,.55), 0 0 0 1px rgba(0,0,0,.15);
  }
  .site-title {
    position: absolute; left: 43px; top: 23px;
    font-family: "Didact Gothic", "Century Gothic", sans-serif;
    font-size: 38px; font-weight: 400; color: var(--white);
  }
  .hero {
    position: absolute; left: 43px; top: 72px; width: 864px; height: 246px;
    background: linear-gradient(to right, #a00000 0, var(--red) 100%);
    overflow: hidden;
  }
  .hero-photo {
    position: absolute; left: 0; top: 0; width: 470px; height: 246px;
    background: linear-gradient(to right, #f2f2f2 0%, #d9d9d9 45%, #c9c9c9 68%, rgba(170,0,0,0) 100%);
  }
  .hero-heading {
    position: absolute; left: 444px; top: 6px;
    font-family: "Didact Gothic", "Century Gothic", sans-serif;
    font-size: 47px; line-height: 57px; font-weight: 400; color: var(--white);
  }
  .hero-quote {
    position: absolute; left: 444px; top: 148px; width: 410px;
    font-style: italic; font-size: 16.5px; line-height: 21px; color: var(--white);
  }
  .hero-strip { position: absolute; left: 0; bottom: 0; }
  .login { position: absolute; left: 43px; top: 345px; width: 260px; }
  .section-title { font-weight: 700; font-size: 27px; color: var(--white); }
  .login-row { display: flex; align-items: center; margin-top: 12px; }
  .login-row:first-of-type { margin-top: 14px; }
  .login-row label { width: 80px; font-size: 13px; font-weight: 700; }
  .login-row input { width: 130px; height: 17px; border: 1px solid var(--grey); background: var(--white); }
  .login-actions { display: flex; gap: 6px; margin-left: 80px; margin-top: 13px; }
  .login-actions button {
    font-family: "Noto Sans", Verdana, sans-serif; font-size: 12px; color: var(--red);
    background: var(--white); border: 1px solid var(--grey); padding: 1px 6px; height: 20px;
  }
  .news { position: absolute; left: 307px; top: 345px; width: 600px; }
  .news-item { margin-top: 12px; font-size: 12px; line-height: 15px; font-style: italic; }
  .news-item:first-of-type { margin-top: 16px; }
  .news-date { font-style: normal; font-weight: 700; margin-right: 12px; }
  .site-footer {
    position: absolute; left: 130px; top: 752px; width: 940px;
    display: flex; justify-content: space-between; font-size: 11px; color: var(--footer-text);
  }
  .site-footer ul { list-style: none; display: flex; gap: 14px; }
  .site-footer a { color: var(--footer-text); text-decoration: none; }
</style>
</head>
<body>
  <nav class="top-nav">
    <ul>
      <li class="nav-about"><a href="#">About Blue Falcons</a></li>
      <li class="nav-services"><a href="#">Services &amp; Solutions</a></li>
      <li class="nav-results"><a href="#">Results</a></li>
      <li class="nav-news"><a href="#">News &amp; Announcements</a></li>
      <li class="nav-contact"><a href="#">Contact Us</a></li>
    </ul>
  </nav>

  <main class="main-panel">
    <h1 class="site-title">Blue Falcons</h1>

    <section class="hero">
      <div class="hero-photo" role="img" aria-label="Photo of a crowd of white spheres with one standing-out red sphere"></div>
      <h2 class="hero-heading">Blue Falcons<br>Lead Generation</h2>
      <p class="hero-quote">“Lorem ipsum dolor sit amet, consectetur adipisicing elit, sed do eiusmod tempor incididunt ut labore et dolore magna aliqua.”</p>
      <svg class="hero-strip" width="864" height="40" viewBox="0 0 864 40">
        <path d="M0 40 L0 34 Q430 30 700 18 Q760 16 864 16 L864 40 Z" fill="#ffffff"/>
        <path d="M0 34 Q430 30 700 18 Q760 16 864 16" fill="none" stroke="#dddddd" stroke-width="1"/>
        <circle cx="770" cy="30" r="7" fill="#aa0000"/>
        <circle cx="789" cy="30" r="7" fill="#cccccc"/>
        <circle cx="808" cy="30" r="7" fill="#cccccc"/>
        <circle cx="827" cy="30" r="7" fill="#cccccc"/>
        <circle cx="846" cy="30" r="7" fill="#cccccc"/>
      </svg>
    </section>

    <section class="login">
      <h2 class="section-title">User login</h2>
      <div class="login-row"><label for="user">User name:</label><input id="user" type="text"></div>
      <div class="login-row"><label for="pass">Password:</label><input id="pass" type="password"></div>
      <div class="login-actions"><button type="button">Login</button><button type="button">Register</button></div>
    </section>

    <section class="news">
      <h2 class="section-title">News &amp; Announcements</h2>
      <p class="news-item"><span class="news-date">27 07 2011</span>"Lorem ipsum dolor sit amet, consectetur adipisicing elit, sed do eiusmod tempor incididunt ut labore et dolore magna aliqua. Ut enim ad minim veniam, quis nostrud exercitation ullamco laboris nisi ut aliquip ex ea commodo consequat."</p>
      <p class="news-item"><span class="news-date">27 07 2011</span>Duis aute irure dolor in reprehenderit in voluptate velit esse cillum dolore eu fugiat nulla pariatur. Excepteur sint occaecat cupidatat non proident, sunt in culpa qui officia deserunt mollit anim id est laborum.</p>
      <p class="news-item"><span class="news-date">26 07 2011</span>The standard chunk of Lorem Ipsum used since the 1500s is reproduced below for those interested. Sections 1.10.32 and 1.10.33 from "de Finibus Bonorum et Malorum" by Marcus Olvan are also reproduced in their exact original form, accompanied by English versions from the 1914 translation by H. Pellworth.</p>
      <p class="news-item"><span class="news-date">25 07 2011</span>1.10.32 and 1.10.33 of "de Finibus Bonorum et Malorum" (The Extremes of Good and Evil) by Marcus Olvan, written in 45 BC.</p>
    </section>
  </main>

  <footer class="site-footer">
    <span>Copyright © 2011 Blue Falcons. All Rights Reserved.</span>
    <ul>
      <li><a href="#">About Blue Falcons</a></li>
      <li><a href="#">Services &amp; Solutions</a></li>
      <li><a href="#">Results</a></li>
      <li><a href="#">News &amp; Announcements</a></li>
      <li><a href="#">Contact Us</a></li>
    </ul>
  </footer>
</body>
</html>
```